Political Mail Out Quintero front and back

Front
Esteban (9th Grade) Quintero!

What's that famous saying?

Show me who your friends are and I'll tell you who you really are!
(show the two guys)

Arturo Benavides is charged with voter fraud by changing voter addresses from across the RGV so they could vote in Edinburg
Back
Did Esteban (9th Grade) Quintero commit voter fraud when he ran for office in 2016?
(insert blurred photo)

Here is a list of people from all over the RGV that voted in Edinburg in the 2016 race.
Here is a break down:

(highlight the number and where they were first registered to vote)

9 People voted in Edinburg who were registered in Donna.
13 People voted in Edinburg who were registered in San Juan
8 People voted in Edinburg who were registered in Pharr
31 People voted in Edinburg who were registered in McAllen
2 People voted in Edinburg who were registered in La Joya
6 People voted in Edinburg who were registered in Edcouch
2 People voted in Edinburg who were registered in Mercedes
2 People voted in Edinburg who were registered in Monte Alto
6 People voted in Edinburg who were registered in Weslaco
1 Person voted in Edinburg who were registered in Penitas
3 People voted in Edinburg who were registered in Alamo
5 People voted in Edinburg who were registered in Elsa
6 People voted in Edinburg who were registered in Mission
1 Person voted in Edinburg who were registered in Alton

Will Esteban (9th Grade) Quintero CHEAT in 2020?

Only time will tell.

Vote Esteban (9th Grade) Quintero OUT of office.

```html
<!DOCTYPE html>
<html lang="en">
<head>
<meta charset="utf-8">
<title>Quintero Mail Out – Front and Back</title>
<link rel="stylesheet" href="https://fonts.googleapis.com/css2?family=Oswald:wght@400;500;600;700&family=Poppins:wght@400;700&display=swap">
<style>
  :root {
    --stage: #3a3a3c;
    --paper: #ffffff;
    --paper-shade: #ececec;
    --red: #e3161e;
    --ink: #3b3b3d;
    --ink-dark: #1c1c1e;
  }
  * { box-sizing: border-box; margin: 0; padding: 0; }
  html, body { width: 1200px; height: 776px; overflow: hidden; }
  body {
    background: var(--stage);
    font-family: "Oswald", sans-serif;
    position: relative;
  }
  .card {
    position: absolute;
    top: 63px;
    width: 500px;
    height: 650px;
    overflow: hidden;
    background: linear-gradient(160deg, var(--paper) 55%, var(--paper-shade) 100%);
  }
  .card--front { left: 70px; }
  .card--back { left: 630px; }

  /* Front */
  .title {
    position: absolute; top: 48px; left: 0; width: 100%;
    display: flex; justify-content: center; align-items: center; gap: 10px;
    color: var(--red); font-weight: 600; font-size: 48px; text-transform: uppercase; line-height: 1;
  }
  .title__grade {
    display: flex; flex-direction: column; align-items: center;
    color: var(--ink); font-size: 21px; font-weight: 500; line-height: 0.95;
  }
  .saying-frame {
    position: absolute; top: 150px; left: 30px; width: 440px; height: 250px;
    border: 3px solid var(--ink-dark);
  }
  .saying-frame__label {
    position: absolute; top: -15px; left: 50%; transform: translateX(-50%);
    background: var(--paper); padding: 0 12px; white-space: nowrap;
    color: var(--red); font-size: 20px; font-weight: 500; text-transform: uppercase;
  }
  .saying-frame__quote {
    position: absolute; top: 24px; left: 0; width: 100%; text-align: center;
    color: var(--ink); font-size: 24px; font-weight: 500; line-height: 1.15; text-transform: uppercase;
  }
  .friends-photo {
    position: absolute; top: 258px; left: 55px; width: 415px; height: 238px;
    border: 4px solid var(--red);
    background: linear-gradient(100deg, #e6d8cc 0%, #8a7160 35%, #6e6e70 65%, #3d3430 100%);
  }
  .charge {
    position: absolute; top: 540px; left: 15px; width: 470px; text-align: center;
    color: var(--red); font-size: 15px; font-weight: 500; line-height: 1.45; text-transform: uppercase;
    white-space: nowrap;
  }

  /* Back */
  .question {
    position: absolute; top: 48px; left: 36px; width: 220px; height: 108px;
    border: 4px solid var(--ink); padding: 12px 16px;
    color: var(--ink); font-size: 17px; font-weight: 500; line-height: 1.25; text-transform: uppercase;
    background: var(--paper);
  }
  .records-photo {
    position: absolute; top: 30px; left: 245px; width: 215px; height: 145px;
    border: 4px solid var(--red);
    background: linear-gradient(90deg, #9c9c9c 0%, #d6d6d6 40%, #c4c4c4 100%);
  }
  .breakdown-heading {
    position: absolute; top: 192px; left: 30px; width: 440px; text-align: center;
    color: var(--red); font-size: 15px; font-weight: 500; line-height: 1.3; text-transform: uppercase;
  }
  .breakdown {
    position: absolute; top: 242px; left: 40px; width: 420px; list-style: none;
    font-family: "Poppins", sans-serif; font-size: 12.5px; line-height: 18px; color: var(--ink-dark);
  }
  .breakdown li { display: flex; gap: 6px; }
  .breakdown .count { font-weight: 700; width: 72px; white-space: nowrap; }
  .breakdown .detail { flex: 1; display: flex; justify-content: space-between; }
  .breakdown .place { font-weight: 700; }
  .cheat {
    position: absolute; top: 506px; left: 0; width: 100%; text-align: center;
    color: var(--red); font-size: 21px; font-weight: 600; text-transform: uppercase; white-space: nowrap;
  }
  .verdict {
    position: absolute; top: 562px; left: 36px; width: 428px; height: 62px;
    border: 3px solid var(--red);
  }
  .verdict__label {
    position: absolute; top: -18px; left: 50%; transform: translateX(-50%);
    background: var(--paper); padding: 0 10px; white-space: nowrap;
    color: var(--red); font-size: 24px; font-weight: 600; text-transform: uppercase; line-height: 1.3;
  }
  .verdict__call {
    position: absolute; top: 20px; left: 0; width: 100%; text-align: center;
    color: var(--ink); font-size: 19px; font-weight: 500; text-transform: uppercase; white-space: nowrap; line-height: 1.3;
  }
</style>
</head>
<body>
  <section class="card card--front">
    <h1 class="title">
      <span>Esteban</span>
      <span class="title__grade"><span>9th</span><span>Grade</span></span>
      <span>Quintero!</span>
    </h1>
    <div class="saying-frame">
      <p class="saying-frame__label">What's that famous saying?</p>
      <p class="saying-frame__quote">Show me who your friends are and<br>I'll tell you who you really are!</p>
    </div>
    <div class="friends-photo" role="img" aria-label="Photo of the two men smiling together, arm in arm"></div>
    <p class="charge">Arturo Benavides is charged with voter fraud by changing voter<br>addresses from across the RGV so they could vote in Edinburg</p>
  </section>

  <section class="card card--back">
    <div class="records-photo" role="img" aria-label="Blurred photo of the voter record printout"></div>
    <p class="question">Did Esteban (9th Grade) Quintero commit voter fraud when he ran for office in 2016?</p>
    <p class="breakdown-heading">Here is a list of people from all over the RGV that voted in<br>Edinburg in the 2016 race. Here is a break down:</p>
    <ul class="breakdown">
      <li><span class="count">9 People</span><span class="detail"><span>voted in Edinburg who were registered in</span><span class="place">Donna.</span></span></li>
      <li><span class="count">13 People</span><span class="detail"><span>voted in Edinburg who were registered in</span><span class="place">San Juan</span></span></li>
      <li><span class="count">8 People</span><span class="detail"><span>voted in Edinburg who were registered in</span><span class="place">Pharr</span></span></li>
      <li><span class="count">31 People</span><span class="detail"><span>voted in Edinburg who were registered in</span><span class="place">McAllen</span></span></li>
      <li><span class="count">2 People</span><span class="detail"><span>voted in Edinburg who were registered in</span><span class="place">La Joya</span></span></li>
      <li><span class="count">6 People</span><span class="detail"><span>voted in Edinburg who were registered in</span><span class="place">Edcouch</span></span></li>
      <li><span class="count">2 People</span><span class="detail"><span>voted in Edinburg who were registered in</span><span class="place">Mercedes</span></span></li>
      <li><span class="count">2 People</span><span class="detail"><span>voted in Edinburg who were registered in</span><span class="place">Monte Alto</span></span></li>
      <li><span class="count">6 People</span><span class="detail"><span>voted in Edinburg who were registered in</span><span class="place">Weslaco</span></span></li>
      <li><span class="count">1 Person</span><span class="detail"><span>voted in Edinburg who were registered in</span><span class="place">Penitas</span></span></li>
      <li><span class="count">3 People</span><span class="detail"><span>voted in Edinburg who were registered in</span><span class="place">Alamo</span></span></li>
      <li><span class="count">5 People</span><span class="detail"><span>voted in Edinburg who were registered in</span><span class="place">Elsa</span></span></li>
      <li><span class="count">6 People</span><span class="detail"><span>voted in Edinburg who were registered in</span><span class="place">Mission</span></span></li>
      <li><span class="count">1 Person</span><span class="detail"><span>voted in Edinburg who were registered in</span><span class="place">Alton</span></span></li>
    </ul>
    <p class="cheat">Will Esteban (9th Grade) Quintero cheat in 2020?</p>
    <div class="verdict">
      <p class="verdict__label">Only time will tell.</p>
      <p class="verdict__call">Vote Esteban (9th Grade) Quintero out of office.</p>
    </div>
  </section>
</body>
</html>
```